Sleek business card design for digital agency.

Brief document attached for detailed description and inspiration. Looking for a minimalist sleek, cool, modern business card design.

Industry/Entity Type

Digital

```html
<!DOCTYPE html>
<html lang="en">
<head>
<meta charset="utf-8">
<title>Kestrel Works – Business Card</title>
<link href="https://fonts.googleapis.com/css2?family=Open+Sans:wght@400;600;700;800&display=swap" rel="stylesheet">
<style>
  :root {
    --page-bg: #e9e6e1;
    --card-grey: #404040;
    --card-band: #535353;
    --card-black: #0c0c0c;
    --back-grey: #474747;
    --mark-dark: #161616;
    --mark-faint: #3b3b3b;
    --text-white: #f2f2f2;
    --text-light: #cfcfcf;
    --card-shadow: rgba(0,0,0,0.25);
  }
  * { box-sizing: border-box; margin: 0; padding: 0; }
  html, body {
    width: 1200px; height: 720px; overflow: hidden;
    background: var(--page-bg);
    font-family: "Open Sans", Arial, sans-serif;
  }
  .canvas {
    position: relative; width: 1200px; height: 720px;
    display: flex; align-items: center; justify-content: center; gap: 50px;
  }
  .card {
    width: 520px; height: 300px; border-radius: 4px; overflow: hidden;
    box-shadow: 0 8px 22px var(--card-shadow);
    position: relative;
  }
  /* Front */
  .card-front { background: var(--card-grey); display: flex; flex-direction: column; }
  .front-brand {
    height: 118px; display: flex; align-items: center; justify-content: center; gap: 14px;
  }
  .brand-dot { width: 34px; height: 34px; border-radius: 50%; background: var(--mark-dark); }
  .brand-name {
    font-weight: 800; font-size: 40px; color: var(--mark-dark); letter-spacing: -0.5px;
  }
  .front-name-band {
    height: 46px; background: var(--card-band);
    display: flex; align-items: center; justify-content: center;
    color: var(--text-white); font-size: 17px;
  }
  .person-name { font-weight: 700; letter-spacing: 0.5px; }
  .person-role { font-weight: 400; font-size: 14px; margin-left: 6px; letter-spacing: 0.3px; }
  .front-contact {
    flex: 1; background: var(--card-black); color: var(--text-light);
    display: flex; flex-direction: column; align-items: center; justify-content: center; gap: 9px;
    font-size: 13px;
  }
  .contact-row { display: flex; gap: 18px; align-items: center; }
  .contact-item { display: flex; align-items: center; gap: 6px; }
  .contact-item svg { width: 13px; height: 13px; fill: var(--text-light); }
  .social-square { width: 12px; height: 12px; background: var(--text-light); border-radius: 2px; }
  .address { font-size: 14px; letter-spacing: 1.2px; margin-top: 4px; }
  /* Back */
  .card-back { background: var(--back-grey); display: flex; align-items: center; justify-content: center; }
  .back-circle {
    position: absolute; width: 130px; height: 130px; border-radius: 50%;
    background: var(--mark-faint); left: 220px; top: 70px;
  }
  .back-brand {
    position: relative; font-weight: 800; font-size: 58px; color: var(--mark-dark); letter-spacing: -1px;
  }
</style>
</head>
<body>
<main class="canvas">
  <section class="card card-front">
    <div class="front-brand">
      <span class="brand-dot"></span>
      <span class="brand-name">Kestrel Works</span>
    </div>
    <div class="front-name-band">
      <span class="person-name">DANIEL HAYES,</span><span class="person-role">MARKETING DIRECTOR</span>
    </div>
    <div class="front-contact">
      <div class="contact-row">
        <span class="contact-item">
          <svg viewBox="0 0 16 16" aria-hidden="true"><path d="M3 1l3 0 1 4-2 1c1 2 3 4 5 5l1-2 4 1 0 3c0 1-1 2-2 2C7 15 1 9 1 3c0-1 1-2 2-2z"/></svg>
          0400 118 272
        </span>
        <span class="contact-item">
          <svg viewBox="0 0 16 16" aria-hidden="true"><rect x="4" y="1" width="8" height="14" rx="1.5"/><rect x="6" y="3" width="4" height="7" fill="#0c0c0c"/></svg>
          03 9000 4816
        </span>
        <span class="contact-item">
          <svg viewBox="0 0 16 16" aria-hidden="true"><rect x="1" y="3" width="14" height="10" rx="1"/><path d="M1.5 3.5l6.5 5 6.5-5" stroke="#0c0c0c" stroke-width="1.4" fill="none"/></svg>
          dhayes@kestrelworks.com
        </span>
      </div>
      <div class="contact-row">
        <span class="contact-item"><span class="social-square"></span>KestrelWorks</span>
        <span class="contact-item"><span class="social-square"></span>@dhayes21</span>
      </div>
      <div class="address">Level 2, 18 Garnet St, Northbank NSW 2000</div>
    </div>
  </section>

  <section class="card card-back">
    <span class="back-circle"></span>
    <span class="back-brand">Kestrel Works</span>
  </section>
</main>
</body>
</html>
```